Real Estate Website

Please refer to the attached document. It will be for a real estate agency specialising in commercial and residential sales. looking for Modern and minimalist, Sleek, professional, premium feel

```html
<!DOCTYPE html>
<html lang="en">
<head>
<meta charset="utf-8">
<title>Ardent Vale Group — Commercial, Industrial &amp; Residential Property</title>
<link href="https://fonts.googleapis.com/css2?family=Oswald:wght@500;600&family=Inter:ital,wght@0,400;0,500;0,600;0,700;1,400&display=swap" rel="stylesheet">
<style>
:root{
  --orange:#E8492A;
  --orange-soft:#F6D3CB;
  --teal:#1F4E5F;
  --teal-deep:#163544;
  --ink:#1E2B33;
  --muted:#6C7A82;
  --beige:#F7F5F1;
  --mist:#DCE5EA;
  --grey-bg:#F2F4F5;
  --line:#E3E8EB;
  --white:#FFFFFF;
}
*{margin:0;padding:0;box-sizing:border-box}
html,body{width:1200px;height:5372px;overflow:hidden}
body{font-family:"Inter",sans-serif;color:var(--ink);background:var(--white);position:relative}
.abs{position:absolute}
section,header,footer{position:absolute;left:0;width:1200px;overflow:hidden}
.eyebrow{font-family:"Oswald",sans-serif;font-weight:500;color:var(--orange);text-transform:uppercase;letter-spacing:.5px}
.heading{font-weight:600;color:var(--teal);letter-spacing:-.3px}
.body{font-size:10px;line-height:17px;color:var(--muted)}
.btn{display:inline-flex;align-items:center;justify-content:center;background:var(--orange);color:#fff;font-size:9px;font-weight:600;border-radius:2px}
.ph{position:absolute}

/* nav */
.nav{top:0;height:46px;background:#fff;display:flex;align-items:center}
.brand{display:flex;align-items:center;gap:6px;font-weight:700;font-size:16px;color:var(--teal)}
.brand .dot{width:12px;height:12px;border-radius:50%;background:var(--orange)}
.nav .brand{position:absolute;left:219px;top:14px}
.nav ul{position:absolute;left:368px;top:19px;display:flex;gap:26px;list-style:none;font-size:8.5px;color:var(--ink)}
.nav .btn{position:absolute;left:898px;top:14px;width:84px;height:20px;font-size:8px}

/* hero */
.hero{top:46px;height:566px;background:linear-gradient(160deg,#4F8EA8 0%,#6FA8C0 55%,#A9D0DE 100%)}
.hero .tower{left:690px;top:0;width:320px;height:566px;background:linear-gradient(180deg,#7FA3B6 0%,#4C6E82 60%,#3A596B 100%);clip-path:polygon(30% 0,100% 0,88% 100%,10% 100%)}
.hero h1{position:absolute;left:219px;top:112px;font-family:"Oswald",sans-serif;font-weight:500;font-size:35px;line-height:40px;color:#fff;text-transform:uppercase;letter-spacing:.5px}
.hero h2{position:absolute;left:219px;top:196px;font-size:37px;line-height:42px;font-weight:500;color:var(--teal-deep)}
.hero .sub{position:absolute;left:219px;top:292px;font-size:10.5px;color:#234a5a}
.hero .b1{position:absolute;left:219px;top:320px;width:192px;height:33px}
.hero .b2{position:absolute;left:421px;top:320px;width:145px;height:33px;background:var(--teal-deep)}
.review-badge{position:absolute;left:980px;top:42px;width:166px;height:42px;border-radius:10px;background:var(--teal-deep);display:flex;align-items:center;padding-left:14px;gap:6px;color:#fff}
.review-badge b{font-size:16px;font-weight:600}
.review-badge span{font-size:8px;opacity:.8}
.review-badge i{display:inline-block;width:14px;height:14px;border-radius:50%;background:#C9D6DD;border:2px solid var(--teal-deep);margin-left:-6px}
.years{position:absolute;left:716px;top:444px;width:116px;height:54px;background:var(--orange);border-radius:6px;color:#fff;text-align:center;padding-top:9px}
.years b{display:block;font-size:15px;font-weight:600}
.years span{font-size:8px}
.scroll{position:absolute;left:593px;top:510px;width:12px;height:18px;border:1.5px solid #fff;border-radius:6px}

/* appraisal */
.appraisal{top:612px;height:542px;background:var(--beige)}
.appraisal .eyebrow{position:absolute;left:219px;top:84px;font-size:32px}
.appraisal .heading{position:absolute;left:219px;top:124px;font-size:29px;line-height:31px}
.appraisal .lead{position:absolute;left:667px;top:86px;width:300px;font-size:9.5px;line-height:14px;color:var(--muted)}
.appraisal .btn{position:absolute;left:667px;top:140px;width:178px;height:22px;font-size:8.5px}
.appraisal .photo{left:219px;top:208px;width:762px;height:259px;background:linear-gradient(120deg,#3C5F71 0%,#A77C5A 45%,#C96E4C 65%,#EDE3D6 100%)}
.appraisal .caption{position:absolute;left:219px;top:476px;width:762px;text-align:center;font-size:9.5px;line-height:14px;color:var(--muted)}

/* why choose */
.why{top:1154px;height:196px;background:var(--mist)}
.why .eyebrow{position:absolute;left:0;width:1200px;top:40px;text-align:center;font-size:32px;color:var(--teal)}
.why ul{list-style:none}
.why li{position:absolute;top:104px;width:150px;text-align:center;font-size:9px;color:var(--ink)}
.why .ic{display:block;margin:0 auto 14px;width:26px;height:26px;border-radius:50%;background:var(--orange-soft);position:relative}
.why .ic::after{content:"";position:absolute;left:8px;top:8px;width:10px;height:10px;border-radius:50%;border:1.5px solid var(--orange)}

/* what / who */
.what{top:1350px;height:445px;background:#fff}
.deco-pink{position:absolute;background:var(--orange-soft);opacity:.8}
.deco-grey{position:absolute;background:var(--mist)}
.what .photo{left:219px;top:78px;width:349px;height:296px;background:linear-gradient(135deg,#4F7A3A 0%,#8A9A7E 40%,#5C5F63 70%,#30343A 100%)}
.block-title .eyebrow{font-size:32px;display:block}
.block-title .heading{font-size:29px;line-height:30px;display:block;margin-top:4px}
.what .text{position:absolute;left:607px;top:78px;width:375px}
.text p{margin-top:14px}
.text p+p{margin-top:6px}
.readmore{display:block;margin-top:10px;font-size:9.5px;color:var(--orange)}
.who{top:1795px;height:476px;background:#fff}
.who .text{position:absolute;left:219px;top:72px;width:380px}
.who .photo{left:632px;top:67px;width:349px;height:296px;background:linear-gradient(120deg,#3E4650 0%,#7D93A6 45%,#CFD7DE 75%,#E6E9EC 100%)}
.checks{list-style:none;margin-top:10px}
.checks li{display:flex;align-items:center;gap:8px;font-size:9.5px;color:var(--ink);height:22px}
.checks svg{flex:none}

/* services */
.services{top:2271px;height:703px;background:linear-gradient(180deg,#1D4A5C 0%,#24586B 60%,#2D6478 100%)}
.services .eyebrow{position:absolute;left:0;width:1200px;text-align:center;top:40px;font-size:32px;color:#fff}
.services .intro{position:absolute;left:226px;top:90px;width:748px;text-align:center;font-size:10px;line-height:18px;color:#DDE7EC}
.card{position:absolute;width:186px;height:225px;background:#fff;border-radius:3px;padding:40px 24px 0}
.card .ic{position:absolute;left:24px;top:40px;width:30px;height:30px;background:var(--orange-soft);border-radius:3px;display:flex;align-items:center;justify-content:center}
.card h3{margin-top:48px;font-size:11px;line-height:16px;font-weight:600;color:var(--teal-deep)}
.card p{margin-top:8px;font-size:9px;line-height:13px;color:var(--muted)}
.card.quote{background:var(--orange);color:#fff}
.card.quote .ic{background:rgba(255,255,255,.25)}
.card.quote h3{color:#fff;margin-top:44px}
.card.quote p{color:#fff}
.card.quote .field{margin-top:14px;font-size:8.5px;border-bottom:1px solid rgba(255,255,255,.7);padding-bottom:5px}
.card.quote .submit{margin-top:10px;height:26px;background:var(--teal-deep);color:#fff;font-size:9px;display:flex;align-items:center;justify-content:center}

/* why ardent */
.reasons{top:2974px;height:657px;background:#fff}
.centered{position:absolute;left:0;width:1200px;text-align:center}
.reasons .eyebrow{top:50px;font-size:34px}
.reasons .heading{top:98px;font-size:29px;line-height:30px}
.rcard{position:absolute;width:240px;height:168px;background:#fff;border:1px solid var(--line);border-radius:4px;padding:22px 20px 0;overflow:hidden}
.rcard::after{content:"";position:absolute;right:-12px;top:-12px;width:52px;height:52px;background:var(--line);border-radius:10px}
.rcard .ic{width:34px;height:34px;background:var(--teal);border-radius:5px;display:flex;align-items:center;justify-content:center}
.rcard h3{margin-top:20px;font-size:11px;line-height:16px;font-weight:600;color:var(--teal-deep)}
.rcard p{margin-top:10px;font-size:9px;line-height:15px;color:var(--muted)}

/* residential */
.residential{top:3631px;height:595px;background:var(--grey-bg)}
.residential .text{position:absolute;left:216px;top:70px;width:372px}
.residential .tag{display:block;font-size:8px;color:var(--orange);margin-top:2px}
.features{display:grid;grid-template-columns:186px 186px;row-gap:18px;margin-top:28px;margin-left:14px}
.features div{display:flex;align-items:center;gap:10px;font-size:8px;color:var(--ink);line-height:11px}
.features i{flex:none;width:18px;height:18px;border-radius:50%;background:var(--mist)}
.residential .btn{position:absolute;left:219px;top:493px;width:170px;height:32px}
.residential .photo{left:620px;top:163px;width:361px;height:267px;background:linear-gradient(180deg,#7A9CB8 0%,#A9BFCE 40%,#5B6B5A 70%,#2F3A33 100%)}
.loc{position:absolute;left:626px;top:370px;width:120px;height:48px;background:#fff;border-radius:3px;padding:8px 10px}
.loc b{display:block;font-size:14px;color:var(--teal-deep);font-weight:600}
.loc span{font-size:7px;color:var(--muted)}

/* careers */
.careers{top:4226px;height:393px;background:#fff}
.careers .eyebrow{top:80px;font-size:34px}
.careers .heading{top:124px;font-size:27px}
.careers .para{top:168px;left:280px;width:640px;font-size:10px;line-height:18px;color:var(--muted)}
.pills{position:absolute;left:0;width:1200px;top:243px;display:flex;justify-content:center;gap:20px}
.pills span{display:flex;align-items:center;gap:8px;height:30px;padding:0 18px;background:var(--grey-bg);border-radius:3px;font-size:8px;color:var(--ink)}
.pills i{width:10px;height:10px;border-radius:50%;border:1.5px solid var(--teal)}
.careers .btn{position:absolute;left:454px;top:302px;width:292px;height:32px}

/* review */
.review{top:4619px;height:467px;background:var(--grey-bg)}
.review .eyebrow{top:62px;font-size:34px}
.review .heading{top:104px;font-size:28px}
.review .mark{top:164px;font-family:"Oswald",sans-serif;font-size:40px;color:var(--orange);line-height:40px}
.review blockquote{position:absolute;left:340px;width:520px;top:212px;text-align:center;font-style:italic;font-size:18px;line-height:22px;color:#3B4A52}
.review .name{top:308px;font-size:10px;font-weight:600;color:var(--teal)}
.review .role{top:325px;font-size:8.5px;color:var(--muted)}
.dots{position:absolute;left:0;width:1200px;top:357px;display:flex;justify-content:center;align-items:center;gap:6px}
.dots .arr{width:28px;height:28px;border-radius:50%;border:1px solid var(--orange-soft);display:flex;align-items:center;justify-content:center;color:var(--orange);font-size:12px;margin:0 6px}
.dots .arr.on{border-color:var(--orange)}
.dots i{width:4px;height:4px;border-radius:50%;background:var(--orange-soft)}
.dots i.on{width:18px;height:5px;border-radius:3px;background:var(--orange)}

/* footer */
.footer{top:5086px;height:286px;background:var(--teal-deep);color:#C9D6DD}
.footer .brand{position:absolute;left:219px;top:44px;color:#fff}
.footer .about{position:absolute;left:219px;top:80px;width:230px;font-size:9px;line-height:15px}
.social{position:absolute;left:219px;top:155px;display:flex;gap:12px}
.social i{width:20px;height:20px;border-radius:50%;border:1px solid #7E99A6}
.fcol{position:absolute;top:50px;font-size:9px;line-height:22px}
.fcol h4{color:#fff;font-size:10px;font-weight:600;margin-bottom:8px;line-height:14px}
.fcol.contact{line-height:14px}
.fcol.contact p{margin-bottom:9px}
.legal{position:absolute;left:219px;right:219px;top:258px;display:flex;justify-content:space-between;font-size:7.5px;color:#8FA6B1;border-top:1px solid rgba(255,255,255,.12);padding-top:8px}
</style>
</head>
<body>

<header class="nav">
  <div class="brand"><span class="dot"></span>Ardent Vale</div>
  <ul><li>Home</li><li>Commercial/Industrial</li><li>Residential</li><li>Business Sales</li><li>About Us</li><li>Info ▾</li><li>Contact Us</li></ul>
  <span class="btn">Book Appraisal</span>
</header>

<section class="hero">
  <div class="ph tower" role="img" aria-label="Glass office tower seen from below against a blue sky"></div>
  <h1>Specialists in Commercial<br>&amp; Industrial Property,</h1>
  <h2>Trusted in Residential<br>Property</h2>
  <p class="sub">Maximizing Returns, Protecting Investments, Expert Property Advisory</p>
  <span class="btn b1">View Commercial &amp; Industrial</span>
  <span class="btn b2">Explore Residential</span>
  <div class="review-badge"><b>100k</b><span>Review</span><i style="margin-left:4px"></i><i></i><i></i><i></i></div>
  <div class="years"><b>40+ Years</b><span>Trusted By Investors</span></div>
  <div class="scroll"></div>
</section>

<section class="appraisal">
  <div class="eyebrow">Book an Appraisal</div>
  <div class="heading">Discover the Real Value<br>of Your Property</div>
  <p class="lead">Book a confidential consultation today and gain the expert guidance you need to maximise returns and make smarter property decisions.</p>
  <span class="btn">Book a Confidential Consultation</span>
  <div class="ph photo" role="img" aria-label="Hand holding a model house above a table of documents"></div>
  <p class="caption">At Ardent Vale Group, we don't just provide standard appraisals — we deliver strategic, insight-driven reports that uncover the true drivers of your property's worth. Whether it's commercial, industrial, or residential, our expertise ensures you see the full picture. From market trends and rental potential to investment performance and future growth opportunities, our tailored reports give you clarity, confidence, and actionable insights.</p>
</section>

<section class="why">
  <div class="eyebrow">Why Choose Us</div>
  <ul>
    <li style="left:249px"><span class="ic"></span>Sector Expertise</li>
    <li style="left:428px"><span class="ic"></span>Proactive Asset Management</li>
    <li style="left:610px"><span class="ic"></span>Bespoke Solutions</li>
    <li style="left:781px"><span class="ic"></span>Professional Excellence</li>
  </ul>
</section>

<section class="what">
  <div class="deco-pink" style="left:190px;top:345px;width:60px;height:60px"></div>
  <div class="ph photo" role="img" aria-label="Team meeting around a table with an architectural model"></div>
  <div class="text block-title">
    <span class="eyebrow">What We Do</span>
    <span class="heading">Property Management,<br>Sales &amp; Leasing</span>
    <p class="body">At Ardent Vale Group, we specialise in guiding property owners, investors, and landlords through the complexities of managing, selling, leasing, and valuing assets. Our mission is clear: to deliver clarity, confidence, and measurable results at every stage of your property journey.</p>
    <p class="body">We go beyond standardised reports. Our strategic, insight-driven valuations and management solutions uncover the true drivers of your property's performance. From tailored marketing campaigns and compelling listings to confidential negotiations and introductions, we ensure your asset attracts the right tenants, buyers, or investors.</p>
    <span class="readmore">Read more</span>
  </div>
</section>

<section class="who">
  <div class="deco-grey" style="left:922px;top:40px;width:80px;height:70px"></div>
  <div class="deco-pink" style="left:602px;top:335px;width:60px;height:60px"></div>
  <div class="text block-title">
    <span class="eyebrow">Who We Are</span>
    <span class="heading">Your Trusted Partner in<br>Property Success</span>
    <p class="body">At Ardent Vale Group, we are recognised as a trusted authority in commercial and residential property management, sales, and leasing. Property owners, investors, and developers turn to us for our proven expertise, discretion, and consistent results.</p>
    <ul class="checks">
      <li><svg width="12" height="12" viewBox="0 0 12 12"><circle cx="6" cy="6" r="5" fill="none" stroke="#E8492A"/><path d="M3.5 6l1.8 1.8L8.6 4.4" fill="none" stroke="#E8492A" stroke-width="1.2"/></svg>40+ years of trusted experience</li>
      <li><svg width="12" height="12" viewBox="0 0 12 12"><circle cx="6" cy="6" r="5" fill="none" stroke="#E8492A"/><path d="M3.5 6l1.8 1.8L8.6 4.4" fill="none" stroke="#E8492A" stroke-width="1.2"/></svg>Strategic, results-driven approach</li>
      <li><svg width="12" height="12" viewBox="0 0 12 12"><circle cx="6" cy="6" r="5" fill="none" stroke="#E8492A"/><path d="M3.5 6l1.8 1.8L8.6 4.4" fill="none" stroke="#E8492A" stroke-width="1.2"/></svg>Full-service property solutions</li>
      <li><svg width="12" height="12" viewBox="0 0 12 12"><circle cx="6" cy="6" r="5" fill="none" stroke="#E8492A"/><path d="M3.5 6l1.8 1.8L8.6 4.4" fill="none" stroke="#E8492A" stroke-width="1.2"/></svg>Dedicated client partnerships</li>
    </ul>
    <span class="readmore">Read more</span>
  </div>
  <div class="ph photo" role="img" aria-label="Agent shaking hands with a smiling couple"></div>
</section>

<section class="services">
  <div class="eyebrow">Our Services</div>
  <p class="intro">At Ardent Vale Group, we are recognised as a leading authority in the management and leasing of premium commercial and industrial assets. Trusted by investors, landlords, and developers, our portfolio spans medical centres, healthcare facilities, allied health clinics, global franchise brands such as Crumb &amp; Co and The Velvet Bakehouse, high-end retail outlets, and large-scale industrial and manufacturing properties.</p>
  <div class="card" style="left:296px;top:169px"><span class="ic"><svg width="12" height="12" viewBox="0 0 12 12"><path d="M2 5h2l5-3v8L4 7H2z" fill="none" stroke="#E8492A"/></svg></span><h3>Strategic Marketing &amp; Leasing</h3><p>Positioning your property to attract premium tenants through targeted, multi-channel campaigns.</p></div>
  <div class="card" style="left:506px;top:169px"><span class="ic"><svg width="12" height="12" viewBox="0 0 12 12"><circle cx="6" cy="4" r="2.2" fill="none" stroke="#E8492A"/><path d="M2 11c0-2.5 2-4 4-4s4 1.5 4 4" fill="none" stroke="#E8492A"/></svg></span><h3>Tenant &amp; Lease Administration</h3><p>Precision management of agreements, renewals, compliance, and documentation.</p></div>
  <div class="card" style="left:716px;top:169px"><span class="ic"><svg width="12" height="12" viewBox="0 0 12 12"><path d="M1 9l4-4 2 2 4-4" fill="none" stroke="#E8492A"/></svg></span><h3>Revenue Optimisation</h3><p>Proactive rent collection, vacancy minimisation, and lease structuring to elevate asset value.</p></div>
  <div class="card" style="left:296px;top:417px"><span class="ic"><svg width="12" height="12" viewBox="0 0 12 12"><path d="M2 10l5-5M7 2a3 3 0 103 3" fill="none" stroke="#E8492A"/></svg></span><h3>Maintenance &amp; Property Upkeep</h3><p>Access to vetted, high-quality trades for repairs and preventative care, ensuring assets remain in peak condition.</p></div>
  <div class="card" style="left:506px;top:417px"><span class="ic"><svg width="12" height="12" viewBox="0 0 12 12"><path d="M6 1l4 1.5V6c0 2.5-2 4-4 5-2-1-4-2.5-4-5V2.5z" fill="none" stroke="#E8492A"/></svg></span><h3>Regulatory Compliance &amp; Essential Services</h3><p>Full oversight of statutory obligations and essential service measures, protecting both compliance and reputation.</p></div>
  <div class="card quote" style="left:716px;top:417px"><span class="ic"><svg width="12" height="12" viewBox="0 0 12 12"><path d="M2 7V4h3v3L4 9M7 7V4h3v3L9 9" fill="none" stroke="#fff"/></svg></span><h3>Get a Free Property Quote</h3><p>Your details are confidential and used only to prepare your quote.</p><div class="field">Enter Your Email Id</div><div class="submit">Submit</div></div>
</section>

<section class="reasons">
  <div class="eyebrow centered" style="top:50px">Why Ardent Vale Group</div>
  <div class="heading centered" style="top:98px">Why Property Owners Choose<br>Ardent Vale Group</div>
  <div class="rcard" style="left:219px;top:214px"><span class="ic"><svg width="16" height="16" viewBox="0 0 16 16"><circle cx="8" cy="8" r="6" fill="none" stroke="#fff"/><circle cx="8" cy="8" r="2.5" fill="none" stroke="#fff"/></svg></span><h3>Specialised Expertise Across Sectors</h3><p>Deep knowledge in commercial, industrial, and residential markets.</p></div>
  <div class="rcard" style="left:479px;top:214px"><span class="ic"><svg width="16" height="16" viewBox="0 0 16 16"><path d="M2 12l4-4 3 3 5-6" fill="none" stroke="#fff" stroke-width="1.4"/></svg></span><h3>Strategic, Results-Driven Approach</h3><p>Data-informed strategies that maximise your property outcomes.</p></div>
  <div class="rcard" style="left:740px;top:214px"><span class="ic"><svg width="16" height="16" viewBox="0 0 16 16"><path d="M3 7h3l6-3v9L6 10H3z" fill="none" stroke="#fff"/></svg></span><h3>Innovative Marketing &amp; Sale Methods</h3><p>Cutting-edge techniques to attract premium buyers and tenants.</p></div>
  <div class="rcard" style="left:219px;top:406px"><span class="ic"><svg width="16" height="16" viewBox="0 0 16 16"><rect x="4" y="2" width="8" height="12" fill="none" stroke="#fff"/><path d="M6 5h4M6 8h4" stroke="#fff"/></svg></span><h3>Full-Service Property Management &amp; Leasing</h3><p>End-to-end solutions for seamless property operations.</p></div>
  <div class="rcard" style="left:479px;top:406px"><span class="ic"><svg width="16" height="16" viewBox="0 0 16 16"><circle cx="6" cy="6" r="2.2" fill="none" stroke="#fff"/><circle cx="11" cy="6" r="2.2" fill="none" stroke="#fff"/><path d="M2 13c0-2.5 2-3.5 4-3.5s4 1 4 3.5M10 9.5c2 0 4 1 4 3.5" fill="none" stroke="#fff"/></svg></span><h3>Trusted Network of Professionals</h3><p>Access to industry-leading partners and service providers.</p></div>
  <div class="rcard" style="left:740px;top:406px"><span class="ic"><svg width="16" height="16" viewBox="0 0 16 16"><rect x="4" y="2" width="8" height="12" rx="1" fill="none" stroke="#fff"/><circle cx="8" cy="7" r="2" fill="none" stroke="#fff"/></svg></span><h3>Professionalism, Integrity &amp; Innovation</h3><p>Values-driven service that puts your interests first.</p></div>
</section>

<section class="residential">
  <div class="text block-title">
    <span class="eyebrow">Residential Property</span>
    <span class="tag">Where Bayside Lifestyle Meets Property Excellence</span>
    <span class="heading">Residential Property<br>Expertise — Redefined</span>
    <p class="body">We curate lifestyle investments. With 40+ years of local sales experience across Bayside and the Mornington Peninsula, our team consistently delivers premium results in residential property and development projects.</p>
    <div class="features">
      <div><i></i>Lifestyle-Driven Sales Experience</div>
      <div><i></i>Bayside Market Leadership</div>
      <div><i></i>Elite Sales Team &amp; Auctioneers</div>
      <div><i></i>Tailored, High-Impact Marketing</div>
      <div><i></i>Negotiation Excellence</div>
      <div><i></i>End-to-End Partnership</div>
    </div>
  </div>
  <span class="btn">View Residential Listings</span>
  <div class="deco-pink" style="left:598px;top:138px;width:62px;height:60px"></div>
  <div class="deco-grey" style="left:955px;top:400px;width:52px;height:80px"></div>
  <div class="ph photo" role="img" aria-label="Modern waterfront home at dusk with a lit pool"></div>
  <div class="loc"><b>Bayside</b><span>&amp; Mornington Peninsula</span></div>
</section>

<section class="careers">
  <div class="eyebrow centered" style="top:80px">Careers</div>
  <div class="heading centered" style="top:124px">Build Your Future in Real Estate</div>
  <p class="abs para" style="top:168px;left:280px;width:640px;text-align:center;font-size:10px;line-height:18px;color:var(--muted)">We're creating space for ambitious professionals to thrive. Our CEO is deeply passionate about property sales, property management, entrepreneurship, and empowering others to build lasting success. At Ardent Vale Group, we don't just offer employment – we offer an opportunity to build your own business within a trusted, high-performing brand.</p>
  <div class="pills"><span><i></i>Build Your Business</span><span><i></i>Growth &amp; Development</span><span><i></i>Collaborative Culture</span></div>
  <span class="btn">Book a Confidential Appointment with Our CEO</span>
</section>

<section class="review">
  <div class="eyebrow centered" style="top:62px">Review</div>
  <div class="heading centered" style="top:104px">What Our Clients Say</div>
  <div class="centered mark">”</div>
  <blockquote>"As a medical centre owner, finding the right property management partner was critical. Ardent Vale Group has been exceptional in every aspect."</blockquote>
  <div class="centered name">Dr. Nora Lind</div>
  <div class="centered role">Healthcare Property Owner</div>
  <div class="dots"><span class="arr">‹</span><i></i><i></i><i class="on"></i><i></i><i></i><span class="arr on">›</span></div>
</section>

<footer class="footer">
  <div class="brand"><span class="dot"></span>Ardent Vale</div>
  <p class="about">Specialists in commercial, industrial, and residential property management, sales, and leasing. Trusted by investors and property owners for over 40 years.</p>
  <div class="social"><i></i><i></i><i></i><i></i></div>
  <div class="fcol" style="left:542px"><h4>Quick Links</h4>Home<br>About Us<br>Commercial/Industrial<br>Residential<br>Contact</div>
  <div class="fcol" style="left:683px"><h4>Information</h4>Blog<br>Videos<br>Careers<br>Privacy Policy<br>Terms of Service</div>
  <div class="fcol contact" style="left:813px"><h4>Contact</h4><p>48 Wren Lane<br>Eastvale, VIC 3999<br>Australia</p><p>+61 3 0000 1234</p><p>info@ardentvale.example</p></div>
  <div class="legal"><span>© 2025 Ardent Vale Group — All Rights Reserved</span><span>Property Specialists | Melbourne, Australia</span></div>
</footer>

</body>
</html>
```